Business Card Design

Business Card for professional consulting firm working with large financial institutions.

Target Market(s)

Executive buyers

Industry/Entity Type

Banking

Contact Information for Business Card

Mild creativity wanted. Not boring, but do elaborate artwork.

Font styles to use
Serif
Sans Serif

Colors

Designer to choose colors to be used in the design.

Requirements
Must have
• Standard business card features - company name, individual name, telephone, website, email, locations.
Nice to have
• Two colors
Should not have
• too many colors, fancy printing, cartoons.

```html
<!DOCTYPE html>
<html lang="en">
<head>
<meta charset="UTF-8">
<title>Northvale Advisory – Business Card</title>
<link href="https://fonts.googleapis.com/css2?family=Open+Sans:wght@400;600;700&display=swap" rel="stylesheet">
<style>
  :root {
    --backdrop: #3a3a3c;
    --card: #1d1d1f;
    --card-edge: #262628;
    --ink-light: #f2f2f2;
    --ink-soft: #c9c9c9;
    --brand-silver: #bdbdbd;
    --brand-emboss: #2b2b2d;
  }
  * { margin: 0; padding: 0; box-sizing: border-box; }
  html, body {
    width: 799px;
    height: 1200px;
    overflow: hidden;
    background: var(--backdrop);
    font-family: "Open Sans", Arial, sans-serif;
  }
  .sheet {
    width: 799px;
    height: 1200px;
    display: flex;
    flex-direction: column;
    justify-content: space-around;
    align-items: center;
    padding: 60px 0;
  }
  .card {
    position: relative;
    width: 620px;
    height: 354px;
    background: var(--card);
    border: 1px solid var(--card-edge);
    border-radius: 3px;
    box-shadow: 0 10px 24px rgba(0,0,0,0.35);
  }
  .card--front .brand {
    position: absolute;
    left: 0; right: 0; top: 50%;
    transform: translateY(-50%);
    text-align: center;
    color: var(--brand-emboss);
    font-size: 44px;
    font-weight: 600;
    letter-spacing: 0.5px;
    text-shadow: none;
  }
  .card--back .identity {
    position: absolute;
    left: 40px; top: 40px;
  }
  .identity .person-name {
    color: var(--ink-light);
    font-size: 22px;
    font-weight: 700;
  }
  .identity .person-role {
    color: var(--ink-soft);
    font-size: 13px;
    margin-top: 2px;
  }
  .card--back .brand {
    position: absolute;
    right: 40px; top: 150px;
    color: var(--brand-silver);
    font-size: 30px;
    font-weight: 600;
  }
  .contact {
    position: absolute;
    left: 40px; bottom: 40px;
    list-style: none;
    color: var(--ink-light);
    font-size: 15px;
    line-height: 24px;
  }
  .contact li { display: flex; align-items: center; gap: 10px; }
  .contact svg { width: 14px; height: 14px; fill: none; stroke: var(--ink-light); stroke-width: 1.6; }
  .contact .address { margin-top: 2px; }
</style>
</head>
<body>
  <main class="sheet">
    <section class="card card--front" aria-label="Card front">
      <div class="brand">Northvale Advisory</div>
    </section>

    <section class="card card--back" aria-label="Card back">
      <div class="identity">
        <div class="person-name">John Doe Smith</div>
        <div class="person-role">Managing Director</div>
      </div>

      <div class="brand">Northvale Advisory</div>

      <ul class="contact">
        <li>
          <svg viewBox="0 0 16 16" aria-hidden="true"><path d="M4 2l2.5 3-1.5 1.5c.8 1.8 2.2 3.2 4 4L10.5 9l3 2.5-1.5 2.5C7 13.5 2.5 9 2 4z"/></svg>
          555.555.5555
        </li>
        <li>
          <svg viewBox="0 0 16 16" aria-hidden="true"><rect x="1.5" y="3.5" width="13" height="9"/><path d="M1.5 3.5L8 9l6.5-5.5"/></svg>
          johndoe@example.com
        </li>
        <li>
          <svg viewBox="0 0 16 16" aria-hidden="true"><circle cx="8" cy="8" r="6.5"/><path d="M1.5 8h13M8 1.5c-3 3.5-3 9.5 0 13M8 1.5c3 3.5 3 9.5 0 13"/></svg>
          www.yourwebsite.com
        </li>
        <li class="address">234 Anywhere St., Any Town, US 123456</li>
      </ul>
    </section>
  </main>
</body>
</html>
```